Assisted living facility needs a business card design

We need a business card design for an assisted living facility in Los Angeles. We have a logo selected but we would like a business card design that will leave a lasting impression on families looking to place their elderly loved ones in our care as well as on other facility providers who may refer their elderly residents to our facility.

```html
<!DOCTYPE html>
<html lang="en">
<head>
<meta charset="utf-8">
<title>Harborview Crest Senior Living – Business Card</title>
<link href="https://fonts.googleapis.com/css2?family=Cinzel:wght@400;700&family=Montserrat:wght@400;500&display=swap" rel="stylesheet">
<style>
  :root {
    --backdrop: #3b3b3d;
    --card: #161617;
    --blue: #0a5fb0;
    --blue-bright: #1a73c8;
    --grey: #7a7a7c;
    --white: #f2f2f2;
  }
  * { margin: 0; padding: 0; box-sizing: border-box; }
  html, body { width: 1200px; height: 801px; overflow: hidden; background: var(--backdrop); }
  .canvas { position: relative; width: 1200px; height: 801px; }

  .card {
    position: absolute;
    left: 300px;
    width: 600px;
    height: 343px;
    background: var(--card);
    border-radius: 18px;
    overflow: hidden;
  }
  .card--front { top: 38px; }
  .card--back { top: 420px; }

  .brand-name {
    position: absolute;
    font-family: "Cinzel", serif;
    font-weight: 400;
    color: var(--blue-bright);
    text-transform: uppercase;
    text-align: center;
    line-height: 1.15;
  }
  .card--front .brand-name {
    left: 0; right: 0; top: 128px;
    font-size: 34px;
    letter-spacing: 2px;
  }
  .card--front .brand-name small {
    display: block;
    font-size: 15px;
    letter-spacing: 7px;
    margin-top: 8px;
  }
  .card--back .brand-name {
    left: 24px; width: 340px; top: 150px;
    font-size: 21px;
    letter-spacing: 1px;
  }
  .card--back .brand-name small {
    display: block;
    font-size: 10px;
    letter-spacing: 5px;
    margin-top: 5px;
  }

  .divider {
    position: absolute;
    left: 382px; top: 40px;
    width: 2px; height: 180px;
    background: var(--blue);
  }

  .contact {
    position: absolute;
    left: 400px; top: 40px;
    font-family: "Montserrat", sans-serif;
    color: var(--white);
  }
  .contact__name {
    font-family: "Cinzel", serif;
    font-weight: 700;
    font-size: 19px;
    color: var(--blue-bright);
    letter-spacing: 0.5px;
  }
  .contact__title { font-size: 12px; margin-top: 2px; }
  .contact__list { list-style: none; margin-top: 16px; font-size: 11.5px; }
  .contact__list li { display: flex; align-items: center; gap: 7px; margin-bottom: 6px; }
  .contact__list svg { width: 11px; height: 11px; fill: var(--blue-bright); flex: none; }
  .contact__address { margin-top: 16px; font-size: 11.5px; line-height: 1.45; }

  .wave { position: absolute; inset: 0; width: 600px; height: 343px; }
</style>
</head>
<body>
<main class="canvas">

  <section class="card card--front" aria-label="Card front">
    <p class="brand-name">Harborview Crest<small>Senior Living</small></p>
  </section>

  <section class="card card--back" aria-label="Card back">
    <svg class="wave" viewBox="0 0 600 343" aria-hidden="true">
      <path d="M215,343 C380,336 470,292 530,264 C560,250 585,242 600,240 L600,343 Z" fill="var(--blue)"/>
      <path d="M240,336 C390,326 470,282 528,255 C560,240 585,233 600,231 L600,236 C584,238 562,245 531,259 C472,287 392,330 240,336 Z" fill="var(--grey)"/>
    </svg>

    <p class="brand-name">Harborview Crest<small>Senior Living</small></p>

    <div class="divider"></div>

    <div class="contact">
      <p class="contact__name">Daniel Reyes</p>
      <p class="contact__title">Managing Director</p>
      <ul class="contact__list">
        <li><svg viewBox="0 0 24 24"><path d="M6.6 10.8a15 15 0 0 0 6.6 6.6l2.2-2.2c.3-.3.7-.4 1-.2 1.1.4 2.3.6 3.6.6.6 0 1 .4 1 1V20c0 .6-.4 1-1 1A17 17 0 0 1 3 4c0-.6.4-1 1-1h3.5c.6 0 1 .4 1 1 0 1.3.2 2.5.6 3.6.1.3 0 .7-.2 1z"/></svg>123 456 789</li>
        <li><svg viewBox="0 0 24 24"><path d="M2 5h20v14H2z M2 5l10 8 10-8"/></svg>info@harborviewcrest.com</li>
        <li><svg viewBox="0 0 24 24"><circle cx="12" cy="12" r="10"/></svg>www.harborviewcrest.com</li>
      </ul>
      <p class="contact__address">Your address, City<br>State, Zip 1234</p>
    </div>
  </section>

</main>
</body>
</html>
```